web page design with coding

We are a start up insurance agency who needs to design a full functional web page. we recently did a postcard design though artmeadow I will upload the final project for you to see the color scheme/font we would like to continue to use. I also have a rough draft of verbage I would like our website to have. I will upload that as well.

Reason: I am sorry but the person who will make the final decision on the website is out of the country at the moment and will make the final decision when he returns.

Industry/Entity Type

Insurance

Coding

Coded - Design and coding required

```html
<!DOCTYPE html>
<html lang="en">
<head>
<meta charset="utf-8">
<title>Harbor Insurance Group</title>
<link rel="stylesheet" href="https://fonts.googleapis.com/css2?family=Play:wght@400;700&family=Open+Sans:wght@400;600;700&display=swap">
<style>
:root{
  --navy:#1a3d6e;
  --navy-dark:#1f2b45;
  --green:#2e8540;
  --green-soft:rgba(46,133,64,.82);
  --ink:#1e1e1e;
  --muted:#b5bcc4;
  --line:#e3e3e3;
  --ring:#efefef;
  --grey-bg:#eeeeee;
  --black:#111111;
  --white:#ffffff;
}
*{margin:0;padding:0;box-sizing:border-box}
html,body{width:1200px;height:2848px;overflow:hidden}
body{position:relative;background:var(--white);font-family:"Open Sans",Arial,sans-serif;color:var(--ink)}
.abs{position:absolute}
.heading{font-family:"Play",Arial,sans-serif;font-weight:400}

/* header */
.topbar{left:0;top:0;width:1200px;height:68px;background:var(--navy);z-index:2}
.brand-name{left:110px;top:0;height:68px;display:flex;align-items:center;z-index:3;font-family:"Play",Arial,sans-serif;font-weight:700;font-size:22px;color:var(--white)}
.main-nav{right:48px;top:0;height:68px;display:flex;gap:30px;align-items:center;z-index:3}
.main-nav a{color:var(--white);text-decoration:none;font-size:13px;font-weight:700;letter-spacing:.2px;position:relative}
.main-nav a.current::before{content:"";position:absolute;left:0;right:0;top:-8px;height:2px;background:var(--white)}
.main-nav a.current::after{content:"";position:absolute;left:0;right:0;bottom:-6px;height:1px;background:var(--white)}

/* hero */
.hero{left:0;top:68px;width:1200px;height:548px;background:radial-gradient(ellipse at 30% 60%,#e9f4f8 0%,#a9d6e6 40%,#58b6d2 100%)}
.hero-title{left:108px;top:250px;font-size:42px;color:var(--navy)}
.hero-sub{left:108px;top:318px;font-size:21px;font-weight:700;line-height:27px;color:#0f2a3a;width:280px}
.btn-solid{display:flex;align-items:center;gap:10px;background:var(--green);color:var(--white);font-size:15px;font-weight:600;padding:0 18px;height:40px}
.hero-btn{left:108px;top:410px}
.hero-card{left:938px;top:393px;width:262px;height:223px;background:var(--green-soft);color:var(--white);padding:22px 26px}
.hero-card h3{font-family:"Play",Arial,sans-serif;font-weight:400;font-size:20px;line-height:26px}
.hero-card p{font-size:15px;font-weight:600;line-height:22px;margin-top:14px}
.btn-outline-light{display:inline-flex;align-items:center;gap:10px;border:1px solid var(--white);color:var(--white);font-size:14px;height:40px;padding:0 14px;margin-top:18px}
.slider-dots{left:564px;top:555px;display:flex;gap:8px}
.slider-dots span{width:11px;height:11px;border-radius:50%;background:var(--navy)}
.slider-dots span.on{background:var(--white);border:2px solid var(--navy)}

/* callback */
.callback-title{left:108px;top:686px;font-size:27px;color:var(--green)}
.callback-text{left:108px;top:740px;width:470px;font-size:15px;line-height:25px}
.phone-input{left:108px;top:828px;width:245px;height:40px;border:1px solid #dcdcdc;font-size:12px;color:#9aa0a6;padding:0 14px;display:flex;align-items:center}
.btn-outline{display:flex;align-items:center;gap:10px;border:1.5px solid var(--navy);color:var(--navy);font-size:15px;font-weight:600;height:40px;padding:0 14px;background:var(--white)}
.callback-btn{left:357px;top:828px}
.radar{left:640px;top:616px}
.call-tag{left:778px;top:733px;width:178px;height:26px;background:var(--navy);color:var(--white);font-size:11px;display:flex;align-items:center;justify-content:center}
.rule{left:0;width:1200px;height:2px;background:var(--line)}

/* products */
.photo{background:linear-gradient(135deg,#e4e8ec,#b9c4cf)}
.eyebrow{font-size:14px;font-weight:700;color:var(--green);text-decoration:underline}
.section-title{font-size:27px;color:var(--navy)}
.body-copy{font-size:15px;line-height:25px}
.service-row{left:629px;top:1362px;display:flex;gap:6px}
.service{width:114px;text-align:center;font-size:11px;color:var(--muted)}
.service svg{display:block;margin:0 auto 6px}
.service.active{color:var(--ink)}

/* testimonials */
.testimonials{left:0;top:2070px;width:1200px;height:413px;background:var(--grey-bg)}
.center{width:1200px;text-align:center}
.avatar{left:548px;top:2186px;width:104px;height:104px;border-radius:50%;background:linear-gradient(135deg,#e6c59a,#b8865b);border:3px solid var(--white)}
.quote-mark{font-family:"Play",Arial,sans-serif;font-size:54px;color:#8aa0b8;line-height:1}
.dots-green{left:567px;top:2430px;display:flex;gap:7px}
.dots-green span{width:11px;height:11px;border-radius:50%;border:1.5px solid var(--green)}
.dots-green span.on{background:var(--green)}

/* contact band */
.contact-band{left:0;top:2483px;width:1200px;height:272px;background:var(--black);color:var(--white)}
.contact-item{display:flex;gap:24px;align-items:center}
.contact-icon{width:70px;height:70px;display:flex;align-items:center;justify-content:center}
.contact-text{font-size:12px;font-weight:600;line-height:20px}

/* footer */
.footer-brand{left:108px;top:2770px;height:64px;display:flex;align-items:center;font-family:"Play",Arial,sans-serif;font-weight:700;font-size:22px;color:var(--navy)}
.socials{left:250px;top:2791px;display:flex;gap:12px}
.socials span{width:24px;height:24px;background:var(--navy-dark)}
.footer-nav{right:48px;top:2780px;display:flex;gap:30px}
.footer-nav a{color:var(--navy);font-size:12px;font-weight:600;text-decoration:none}
.copyright{right:48px;top:2817px;font-size:11px;color:#555}
</style>
</head>
<body>

<header>
  <div class="abs topbar"></div>
  <div class="abs brand-name">Harbor Insurance Group</div>
  <nav class="abs main-nav">
    <a class="current" href="#">HOME</a><a href="#">ABOUT US</a><a href="#">SERVICES</a><a href="#">BLOG</a><a href="#">PROJECTS</a><a href="#">NEWS</a><a href="#">CONTACT</a>
  </nav>
</header>

<section>
  <div class="abs hero" role="img" aria-label="Photo of a red umbrella floating in a blue sky with white clouds"></div>
  <h1 class="abs heading hero-title">Insurances do matter</h1>
  <p class="abs hero-sub">Lorem ipsum dolor sit amet, consectetur.</p>
  <div class="abs btn-solid hero-btn">Get a quote
    <svg width="16" height="16" viewBox="0 0 16 16" fill="none" stroke="#fff" stroke-width="1.5"><path d="M15 1L1 7l5 2 2 6z M15 1L6 9"/></svg>
  </div>
  <div class="abs hero-card">
    <h3>Life insurances<br>for your family</h3>
    <p>Curabitur iaculis ante a nibh vulputate sollicitudin.</p>
    <div class="btn-outline-light">Get a quote
      <svg width="16" height="16" viewBox="0 0 16 16" fill="none" stroke="#fff" stroke-width="1.5"><path d="M15 1L1 7l5 2 2 6z M15 1L6 9"/></svg>
    </div>
  </div>
  <div class="abs slider-dots"><span></span><span class="on"></span><span></span><span></span></div>
</section>

<section>
  <h2 class="abs heading callback-title">Take care of your family</h2>
  <p class="abs callback-text">Lorem ipsum dolor sit amet, consectetur adipiscing elit. Mauris hendrerit fringilla ligula, nec congue leo pharetra in.</p>
  <div class="abs phone-input">Your phone number</div>
  <div class="abs btn-outline callback-btn">Get a phone call
    <svg width="15" height="15" viewBox="0 0 24 24" fill="#1a3d6e"><path d="M6.6 10.8a15 15 0 006.6 6.6l2.2-2.2c.3-.3.7-.4 1-.2 1.1.4 2.3.6 3.6.6.6 0 1 .4 1 1V20c0 .6-.4 1-1 1A17 17 0 013 4c0-.6.4-1 1-1h3.5c.6 0 1 .4 1 1 0 1.3.2 2.5.6 3.6.1.3 0 .7-.2 1z"/></svg>
  </div>
  <svg class="abs radar" width="460" height="346" viewBox="0 0 460 346" fill="none">
    <circle cx="226" cy="166" r="217" stroke="var(--ring)" stroke-width="2"/>
    <circle cx="226" cy="166" r="158" stroke="var(--ring)" stroke-width="2"/>
    <circle cx="226" cy="166" r="58" stroke="#e8e8e8" stroke-width="2"/>
    <circle cx="226" cy="166" r="18" fill="#fff" stroke="#1a3d6e" stroke-width="1.5"/>
    <path d="M221 160c0 6 4 11 11 12l2-2-3-2-1 1c-2-1-4-3-5-5l1-1-2-3z" fill="#1a3d6e"/>
  </svg>
  <div class="abs call-tag">Call us:&nbsp;<b>(305) 555-0147</b></div>
  <div class="abs rule" style="top:963px"></div>
</section>

<section>
  <div class="abs photo" style="left:0;top:1007px;width:583px;height:473px" role="img" aria-label="Photo of an older couple reviewing an insurance policy with an agent"></div>
  <p class="abs eyebrow" style="left:629px;top:1048px">Our Product and Services</p>
  <h2 class="abs heading section-title" style="left:629px;top:1122px">Personal Insurance</h2>
  <p class="abs body-copy" style="left:629px;top:1174px;width:470px">Our Personal Insurance Department provides tailored coverage for your home, autos, boats, and personal and liability protection.</p>
  <div class="abs btn-outline" style="left:634px;top:1280px">Get a quote
    <svg width="16" height="16" viewBox="0 0 16 16" fill="none" stroke="#1a3d6e" stroke-width="1.5"><path d="M15 1L1 7l5 2 2 6z M15 1L6 9"/></svg>
  </div>
  <div class="abs service-row">
    <div class="service active">
      <svg width="40" height="44" viewBox="0 0 40 44" fill="none" stroke="#2e8540" stroke-width="3"><circle cx="14" cy="5" r="3.5" fill="#2e8540" stroke="none"/><path d="M14 11v14h12l5 12"/><path d="M14 18h9"/><path d="M10 20a11 11 0 1015 14"/></svg>
      Personal Insurance</div>
    <div class="service">
      <svg width="40" height="44" viewBox="0 0 40 44" fill="#b5bcc4"><rect x="6" y="4" width="28" height="32" rx="5"/><rect x="10" y="9" width="20" height="12" fill="#fff"/><circle cx="12" cy="29" r="2.5" fill="#fff"/><circle cx="28" cy="29" r="2.5" fill="#fff"/><rect x="8" y="36" width="6" height="5"/><rect x="26" y="36" width="6" height="5"/></svg>
      Travel Insurance</div>
    <div class="service">
      <svg width="40" height="44" viewBox="0 0 40 44" fill="#b5bcc4"><path d="M2 20a18 16 0 0136 0z"/><path d="M20 20v16a4 4 0 01-8 0" fill="none" stroke="#b5bcc4" stroke-width="3"/></svg>
      Life Insurance</div>
    <div class="service">
      <svg width="40" height="44" viewBox="0 0 40 44" fill="#b5bcc4"><path d="M9 10h22l5 12v12H4V22z"/><rect x="11" y="13" width="18" height="8" fill="#fff"/><circle cx="11" cy="28" r="2.5" fill="#fff"/><circle cx="29" cy="28" r="2.5" fill="#fff"/><rect x="6" y="34" width="6" height="5"/><rect x="28" y="34" width="6" height="5"/></svg>
      Car Insurance</div>
  </div>
  <div class="abs rule" style="top:1537px"></div>
</section>

<section>
  <p class="abs eyebrow" style="left:108px;top:1646px">About Us</p>
  <h2 class="abs heading section-title" style="left:108px;top:1720px">Harbor Mission Statement</h2>
  <p class="abs body-copy" style="left:108px;top:1772px;width:440px">Harbor Insurance Group is committed to providing the best risk management solutions to fit each client's unique needs. This includes providing creative solutions as if we were seeking insurance for our own family. <span style="color:var(--green);text-decoration:underline">more</span></p>
  <div class="abs photo" style="left:622px;top:1590px;width:578px;height:423px" role="img" aria-label="Photo of two smiling business colleagues working at a laptop"></div>
</section>

<section>
  <div class="abs testimonials"></div>
  <h2 class="abs heading center" style="left:0;top:2110px;font-size:27px;color:var(--navy)">What our clients said</h2>
  <div class="abs avatar" role="img" aria-label="Portrait photo of the client"></div>
  <p class="abs center" style="left:0;top:2303px;font-size:11px;font-weight:700;color:var(--green)">Marina Keller</p>
  <span class="abs quote-mark" style="left:232px;top:2318px">“</span>
  <span class="abs quote-mark" style="left:948px;top:2318px">”</span>
  <p class="abs" style="left:270px;top:2348px;width:660px;text-align:center;font-size:13px;line-height:21px">Thank for such a Support. Quality Support. I'm extremely impressed. It has been one of the best experiences.So pleased with u Harbor.You r d best.</p>
  <div class="abs dots-green"><span></span><span></span><span></span><span class="on"></span></div>
</section>

<section>
  <div class="abs contact-band"></div>
  <p class="abs center" style="left:0;top:2526px;color:var(--white)"><span class="heading" style="font-size:26px">Call us today</span> <span style="font-size:11px;font-weight:700">&nbsp;for your no obligation insurance analysis</span></p>
  <div class="abs contact-item" style="left:108px;top:2614px;color:#fff">
    <div class="contact-icon" style="background:var(--navy)"><svg width="22" height="30" viewBox="0 0 22 30" fill="#fff"><path d="M11 0a11 11 0 00-11 11c0 8 11 19 11 19s11-11 11-19A11 11 0 0011 0zm0 15a4 4 0 110-8 4 4 0 010 8z"/></svg></div>
    <div class="contact-text">1820 Palm Grove Avenue,<br>Suite 310<br>Miami, FL 33101</div>
  </div>
  <div class="abs contact-item" style="left:456px;top:2614px;color:#fff">
    <div class="contact-icon" style="background:var(--green)"><svg width="30" height="30" viewBox="0 0 24 24" fill="#fff"><path d="M6.6 10.8a15 15 0 006.6 6.6l2.2-2.2c.3-.3.7-.4 1-.2 1.1.4 2.3.6 3.6.6.6 0 1 .4 1 1V20c0 .6-.4 1-1 1A17 17 0 013 4c0-.6.4-1 1-1h3.5c.6 0 1 .4 1 1 0 1.3.2 2.5.6 3.6.1.3 0 .7-.2 1z"/></svg></div>
    <div class="contact-text">USA- (305) 555-0147<br>UK- (786) 555-0162<br>AUS- (786) 555-0188</div>
  </div>
  <div class="abs contact-item" style="left:802px;top:2614px;color:#fff">
    <div class="contact-icon" style="background:var(--navy-dark);font-size:30px;font-weight:700">@</div>
    <div class="contact-text">For Query - info@harborig.example<br>For Billing - bills@harborig.example<br>For Support - support@harborig.example</div>
  </div>
</section>

<footer>
  <div class="abs footer-brand">Harbor Insurance Group</div>
  <div class="abs socials" style="left:372px" aria-label="Social links"><span></span><span></span><span></span><span></span></div>
  <nav class="abs footer-nav"><a href="#">HOME</a><a href="#">ABOUT US</a><a href="#">SERVICES</a><a href="#">BLOG</a><a href="#">PROJECTS</a><a href="#">NEWS</a><a href="#">CONTACT</a></nav>
  <p class="abs copyright">Copyright © 2016 All rights Reserved</p>
</footer>

</body>
</html>
```